Design a flyer promoting a baseball tournament, similar to what is attached.
Date: September 16-17th
Location: Denver, CO
Prize: $5k minimum
Name: Walter Brisco Classic
Misc:
* Memorial Scholarship giveaway
* Invite Only
* Sponsored By Pinecrest Hawks
* No entry fee

Target Market(s)

Baseball Teams, Adult

Industry/Entity Type

Recreation

Colors
0455a3
eaf1f7
85cae6

Requirements
Must have
• Tournament Details and info
Nice to have
• dynamic graphics supporting the Denver area landscape

```html
<!DOCTYPE html>
<html lang="en">
<head>
<meta charset="utf-8">
<title>Walter Brisco Classic Baseball Tournament 2017</title>
<link rel="stylesheet" href="https://fonts.googleapis.com/css2?family=Bebas+Neue&display=swap">
<style>
  :root {
    --royal: #0455a3;
    --navy: #1a2768;
    --deep: #111a4a;
    --orange: #f5821f;
    --white: #ffffff;
    --mist: #eaf1f7;
    --sky: #85cae6;
  }
  * { margin: 0; padding: 0; box-sizing: border-box; }
  html, body { width: 849px; height: 1200px; overflow: hidden; background: var(--white); }
  .flyer {
    position: relative;
    width: 849px;
    height: 1200px;
    overflow: hidden;
    font-family: "Bebas Neue", "Arial Narrow", sans-serif;
    color: var(--white);
    background: linear-gradient(160deg, var(--royal) 0%, #1d3f95 45%, var(--deep) 100%);
  }
  .skyline {
    position: absolute;
    left: 0; top: 0;
    width: 849px; height: 600px;
    background:
      linear-gradient(180deg, rgba(0,0,0,0) 40%, rgba(190,120,60,.35) 62%, rgba(0,0,0,0) 78%),
      linear-gradient(180deg, #6a6aa6 0%, #b58ba8 16%, #7c6f9a 28%, #4b5576 42%, #3a3a48 58%, #1a1d26 80%, #0f1218 100%);
  }
  .graphics { position: absolute; left: 0; top: 0; }
  .host {
    position: absolute;
    top: 92px; left: 0; width: 100%;
    text-align: center;
    font-size: 76px;
    line-height: 1;
    letter-spacing: 2px;
  }
  .presents {
    position: absolute;
    top: 214px; left: 0; width: 100%;
    text-align: center;
    font-size: 38px;
    letter-spacing: 1px;
    text-shadow: 0 2px 3px rgba(0,0,0,.6);
  }
  .title {
    position: absolute;
    top: 414px; left: 0; width: 100%;
    text-align: center;
    line-height: 1;
    font-weight: 400;
    text-shadow: 0 3px 2px rgba(0,0,0,.55);
  }
  .title-name { display: block; font-size: 80px; color: var(--orange); letter-spacing: 1px; }
  .title-sub { display: block; font-size: 58px; letter-spacing: 1px; margin-top: 10px; }
  .title-sub + .title-sub { font-size: 60px; letter-spacing: 0; margin-top: 4px; }
  .title-year { display: block; font-size: 54px; color: var(--orange); margin-top: 12px; }
  .date {
    position: absolute;
    top: 820px; left: 0; width: 849px;
    text-align: center;
    font-size: 58px;
    line-height: 1;
    padding-top: 8px;
    text-shadow: 0 3px 2px rgba(0,0,0,.4);
  }
  .prize {
    position: absolute;
    top: 796px; right: 0;
    width: 160px;
    text-align: center;
    line-height: .9;
  }
  .prize-label { display: block; font-size: 36px; margin-top: 12px; }
  .prize-amount { display: block; font-size: 76px; }
  .prize-note { display: block; font-size: 30px; }
  .location {
    position: absolute;
    top: 925px; left: 0; width: 100%;
    text-align: center;
    line-height: 1;
  }
  .location-label { display: block; font-size: 44px; }
  .location-city { display: block; font-size: 90px; margin-top: 4px; letter-spacing: 1px; }
  .details {
    position: absolute;
    left: 0; bottom: 0;
    width: 849px; height: 115px;
    background: var(--orange);
    display: flex;
    align-items: center;
    list-style: none;
  }
  .details li {
    height: 66px;
    display: flex;
    align-items: center;
    justify-content: center;
    text-align: center;
    font-size: 28px;
    line-height: 1;
    border-right: 2px solid var(--white);
  }
  .details li:last-child { border-right: 0; }
  .details .d-scholarship { width: 285px; }
  .details .d-invite { width: 158px; }
  .details .d-fee { width: 172px; }
  .details .d-sponsor { width: 234px; font-size: 26px; }
</style>
</head>
<body>
<main class="flyer">
  <div class="skyline" role="img" aria-label="Photo of the Denver city skyline at dusk with a pink and purple sky and lit towers"></div>

  <svg class="graphics" width="849" height="1200" viewBox="0 0 849 1200">
    <defs>
      <linearGradient id="shieldFill" x1="0" y1="0" x2="1" y2="1">
        <stop offset="0" stop-color="#2a63c4"/>
        <stop offset=".6" stop-color="#1a3a8c"/>
        <stop offset="1" stop-color="#111a4a"/>
      </linearGradient>
      <linearGradient id="batsArea" x1="0" y1="0" x2="0" y2="1">
        <stop offset="0" stop-color="#ffffff" stop-opacity=".22"/>
        <stop offset="1" stop-color="#ffffff" stop-opacity=".14"/>
      </linearGradient>
      <linearGradient id="ballArea" x1="0" y1="0" x2="0" y2="1">
        <stop offset="0" stop-color="#f2f2f2"/>
        <stop offset="1" stop-color="#b8b8b8"/>
      </linearGradient>
    </defs>
    <!-- lower blue field with orange swoosh -->
    <path d="M0,548 C200,610 300,640 425,640 C550,640 650,610 849,548 L849,1200 L0,1200 Z" fill="var(--orange)"/>
    <path d="M0,582 C200,640 300,668 425,668 C550,668 650,640 849,582 L849,1200 L0,1200 Z" fill="#1d49a0"/>
    <!-- crossed bats artwork area -->
    <rect x="168" y="276" width="513" height="534" rx="10" fill="url(#batsArea)" role="img" aria-label="Illustration of two crossed white baseball bats behind the title shield"/>
    <!-- shield -->
    <path d="M142,420 Q150,362 215,360 L634,360 Q699,362 707,420 L726,600 Q728,628 700,640 L424,744 L149,640 Q121,628 123,600 Z" fill="var(--white)"/>
    <path d="M158,424 Q164,376 220,374 L629,374 Q685,376 691,424 L710,598 Q712,620 690,628 L424,728 L159,628 Q137,620 139,598 Z" fill="url(#shieldFill)"/>
    <!-- baseball photo area -->
    <rect x="354" y="268" width="140" height="138" rx="8" fill="url(#ballArea)" role="img" aria-label="Photo of a baseball with red stitching"/>
    <!-- date pill -->
    <path d="M206,822 L640,822 L656,852 L640,882 L206,882 L190,852 Z" fill="none" stroke="var(--white)" stroke-width="1.5" stroke-dasharray="3 2"/>
    <path d="M216,830 L630,830 L644,852 L630,874 L216,874 L202,852 Z" fill="var(--orange)"/>
    <!-- prize tag -->
    <path d="M712,790 L849,790 L849,936 L712,936 L680,863 Z" fill="var(--orange)"/>
  </svg>

  <p class="host">Pinecrest Hawks</p>
  <p class="presents">Presents</p>

  <h1 class="title">
    <span class="title-name">Walter Brisco</span>
    <span class="title-sub">Classic</span>
    <span class="title-sub">Baseball Tournament</span>
    <span class="title-year">2017</span>
  </h1>

  <p class="date">September 16–17th</p>

  <p class="prize">
    <span class="prize-label">Prize</span>
    <span class="prize-amount">$5K</span>
    <span class="prize-note">Minimum</span>
  </p>

  <p class="location">
    <span class="location-label">Location</span>
    <span class="location-city">Denver, CO</span>
  </p>

  <ul class="details">
    <li class="d-scholarship">Memorial<br>Scholarship Giveaway</li>
    <li class="d-invite">Invite Only</li>
    <li class="d-fee">No Entry Fee</li>
    <li class="d-sponsor">Sponsored<br>by Pinecrest Hawks</li>
  </ul>
</main>
</body>
</html>
```